Book cover design for the book titled "Quieter Under Lanterns."

create a book cover. The book title is, "Quieter Under Lanterns: A Ledger of Harbour Songs Across Mild Winters." The purpose of the book is to create awareness of how childhood trauma is impacting 7 out of 10 adults in the world today and that two-thirds of children will experience neglect and or abuse before their 18th birthday. One victim described that his mental and physical illness resulting from childhood trauma felt like he wa being pulled to the ground, that the force was "quieter under lanterns." The design should be clean and simple and communicate a crisis.

```html
<!DOCTYPE html>
<html lang="en">
<head>
<meta charset="utf-8">
<title>Quieter Under Lanterns — Book Cover</title>
<link rel="stylesheet" href="https://fonts.googleapis.com/css2?family=Bebas+Neue&family=Montserrat:wght@600;700&display=swap">
<style>
  :root {
    --page: #ffffff;
    --cover-ink: #231f20;
    --signal-yellow: #fff200;
    --globe-shade: #d9cf00;
    --paper-white: #ffffff;
    --rule-grey: #bdbdbd;
  }
  html, body {
    margin: 0;
    padding: 0;
    width: 1200px;
    height: 1200px;
    overflow: hidden;
    background: var(--page);
  }
  .canvas {
    position: relative;
    width: 1200px;
    height: 1200px;
  }
  .book-cover {
    position: absolute;
    left: 295px;
    top: 141px;
    width: 618px;
    height: 925px;
    background: var(--cover-ink);
  }
  .book-cover svg { display: block; }
  .title-word {
    font-family: "Bebas Neue", "Oswald", sans-serif;
    fill: var(--signal-yellow);
  }
  .title-joiner {
    font-family: "Bebas Neue", "Oswald", sans-serif;
    fill: var(--paper-white);
  }
  .joiner-rule { stroke: var(--rule-grey); stroke-width: 1; }
  .subtitle {
    font-family: "Montserrat", "Helvetica Neue", Arial, sans-serif;
    font-weight: 700;
    fill: var(--paper-white);
  }
  .subtitle .accent { fill: var(--signal-yellow); }
  .author-name {
    font-family: "Montserrat", "Helvetica Neue", Arial, sans-serif;
    font-weight: 600;
    fill: var(--paper-white);
  }
</style>
</head>
<body>
<main class="canvas">
  <section class="book-cover">
    <svg width="618" height="925" viewBox="0 0 618 925" xmlns="http://www.w3.org/2000/svg">
      <defs>
        <radialGradient id="globe-glow" cx="0.45" cy="0.35" r="0.75">
          <stop offset="0" stop-color="var(--signal-yellow)"/>
          <stop offset="1" stop-color="var(--globe-shade)"/>
        </radialGradient>
      </defs>

      <text class="title-word" x="41" y="187" font-size="210" textLength="534" lengthAdjust="spacingAndGlyphs">QUIETER</text>

      <line class="joiner-rule" x1="41" y1="224" x2="240" y2="224"/>
      <text class="title-joiner" x="309" y="242" font-size="55" text-anchor="middle">UNDER</text>
      <line class="joiner-rule" x1="378" y1="224" x2="575" y2="224"/>

      <text class="title-word" x="41" y="410" font-size="210" textLength="534" lengthAdjust="spacingAndGlyphs">LANTERNS</text>

      <text class="subtitle" x="309" y="460" font-size="34" text-anchor="middle" textLength="536" lengthAdjust="spacingAndGlyphs">A LEDGER OF <tspan class="accent">HARBOUR SONGS</tspan></text>
      <text class="subtitle" x="309" y="502" font-size="34" text-anchor="middle" textLength="494" lengthAdjust="spacingAndGlyphs"><tspan class="accent">ACROSS MILD</tspan> WINTERS</text>

      <g role="img" aria-label="Illustration: a yellow globe with a silhouette of a child huddled with knees drawn up, surrounded by four dark hands pointing at her">
        <circle cx="306" cy="695" r="181" fill="url(#globe-glow)"/>
      </g>

      <text class="author-name" x="309" y="914" font-size="32" text-anchor="middle" textLength="300" lengthAdjust="spacing">AUTHOR NAME</text>
    </svg>
  </section>
</main>
</body>
</html>
```